Plumbing & Heating bussiness card design

i do all plumbing and heating work and need a catchy design. keep it simple but eye catching nothing gimicky
i do 24hr call outs
landlord safety checks
all aspects of plumbing and heating
boiler breakdowns
flue sure reg number 804617
i have put up my old card. not to bothered about the front but i have put up the back for the details. mobile number and office are the same and the email has changed to tolwenpipes@mailvoro.net

Industry/Entity Type

Safety

Contact Information for Business Card

i do 24hr call outs
landlord safety checks
boiler breakdowns

Requirements
Must have
• i do 24hr call outs
• landlord safety checks
• all aspects of plumbing and heating
• boiler breakdowns
• flue sure reg number 804617

```html
<!DOCTYPE html>
<html lang="en">
<head>
<meta charset="utf-8">
<title>B Tolwen Plumbing &amp; Heating – Business Cards</title>
<link href="https://fonts.googleapis.com/css2?family=Open+Sans:wght@400;600;700&display=swap" rel="stylesheet">
<style>
  :root {
    --page-bg: #eceae7;
    --card-white: #ffffff;
    --band-top: #2ba6e0;
    --band-bottom: #1d7cc6;
    --ink-dark: #3a3d42;
    --ink-light: #ffffff;
    --ink-soft: #e3f2fb;
    --divider: rgba(255,255,255,0.28);
    --accent-red: #c8202f;
    --badge-fill: rgba(255,255,255,0.9);
  }
  * { box-sizing: border-box; margin: 0; padding: 0; }
  html, body { width: 1200px; height: 900px; overflow: hidden; }
  body {
    background: var(--page-bg);
    font-family: "Open Sans", Arial, sans-serif;
    position: relative;
  }
  .card {
    position: absolute;
    background: var(--card-white);
    box-shadow: 0 6px 18px rgba(0,0,0,0.18);
    overflow: hidden;
  }
  .card--front { left: 78px; top: 34px; width: 588px; height: 364px; }
  .card--back  { left: 388px; top: 505px; width: 567px; height: 352px; }

  .brand {
    position: absolute;
    display: flex;
    align-items: center;
    gap: 14px;
    color: var(--ink-dark);
    font-weight: 600;
  }
  .card--front .brand { left: 32px; top: 78px; }
  .card--back .brand  { left: 36px; top: 84px; }
  .brand__dot {
    width: 22px; height: 22px;
    border-radius: 50%;
    background: var(--accent-red);
    flex: none;
  }
  .brand__name { line-height: 1.05; }
  .brand__main { display: block; font-size: 40px; letter-spacing: 0.5px; }
  .brand__sub  { display: block; font-size: 22px; letter-spacing: 0.8px; margin-top: 2px; }

  .band {
    position: absolute;
    left: 0; right: 0; bottom: 0;
    background: linear-gradient(180deg, var(--band-top), var(--band-bottom));
    color: var(--ink-light);
  }
  .card--front .band { top: 174px; }
  .card--back .band  { top: 193px; }

  .person { position: absolute; left: 30px; top: 18px; }
  .person__name { font-size: 20px; font-weight: 600; }
  .person__role { font-size: 15px; color: var(--ink-soft); margin-top: 0; }

  .contacts {
    position: absolute;
    left: 30px; top: 80px;
    width: 218px;
    list-style: none;
  }
  .contacts__item {
    display: flex; align-items: center; gap: 12px;
    height: 31px;
    font-size: 15px;
    border-bottom: 1px solid var(--divider);
  }
  .contacts__item:last-child { border-bottom: none; }
  .contacts__icon { width: 14px; height: 14px; flex: none; fill: var(--ink-light); }

  .services {
    position: absolute;
    left: 36px; top: 16px;
    list-style: none;
    font-size: 15px;
    font-weight: 600;
  }
  .services li {
    display: flex; align-items: center; gap: 8px;
    height: 23.8px;
  }
  .services li::before {
    content: "";
    width: 7px; height: 7px;
    border-radius: 50%;
    background: var(--ink-light);
  }
  .reg-badge {
    position: absolute;
    right: 47px; top: 50px;
    width: 75px; height: 83px;
    border-radius: 6px;
    background: var(--badge-fill);
  }
</style>
</head>
<body>

  <section class="card card--front" aria-label="Business card front">
    <div class="brand">
      <span class="brand__dot"></span>
      <span class="brand__name">
        <span class="brand__main">B TOLWEN</span>
        <span class="brand__sub">PLUMBING &amp; HEATING</span>
      </span>
    </div>
    <div class="band">
      <div class="person">
        <div class="person__name">Daniel Marsh</div>
        <div class="person__role">Managing Director</div>
      </div>
      <ul class="contacts">
        <li class="contacts__item">
          <svg class="contacts__icon" viewBox="0 0 24 24" aria-hidden="true"><path d="M6.6 10.8a15.1 15.1 0 0 0 6.6 6.6l2.2-2.2c.3-.3.7-.4 1-.2 1.1.4 2.3.6 3.6.6.6 0 1 .4 1 1V20c0 .6-.4 1-1 1A17 17 0 0 1 3 4c0-.6.4-1 1-1h3.5c.6 0 1 .4 1 1 0 1.3.2 2.5.6 3.6.1.3 0 .7-.2 1z"/></svg>
          <span>044-987 654 321</span>
        </li>
        <li class="contacts__item">
          <svg class="contacts__icon" viewBox="0 0 24 24" aria-hidden="true"><path d="M2 5h20v14H2z"/><path d="M3 6.5l9 6.5 9-6.5" fill="none" stroke="var(--band-top)" stroke-width="1.6"/></svg>
          <span>info@tolwenpipes.net</span>
        </li>
        <li class="contacts__item">
          <svg class="contacts__icon" viewBox="0 0 24 24" aria-hidden="true"><path d="M10 14a4 4 0 0 0 5.7 0l3.5-3.5a4 4 0 0 0-5.7-5.7l-1.2 1.2 1.4 1.4 1.2-1.2a2 2 0 0 1 2.9 2.9l-3.5 3.5a2 2 0 0 1-2.9 0zM14 10a4 4 0 0 0-5.7 0l-3.5 3.5a4 4 0 0 0 5.7 5.7l1.2-1.2-1.4-1.4-1.2 1.2a2 2 0 0 1-2.9-2.9l3.5-3.5a2 2 0 0 1 2.9 0z"/></svg>
          <span>www.tolwenpipes.net</span>
        </li>
      </ul>
    </div>
  </section>

  <section class="card card--back" aria-label="Business card back">
    <div class="brand">
      <span class="brand__dot"></span>
      <span class="brand__name">
        <span class="brand__main">B TOLWEN</span>
        <span class="brand__sub">PLUMBING &amp; HEATING</span>
      </span>
    </div>
    <div class="band">
      <ul class="services">
        <li>I do 24hr call outs</li>
        <li>Landlord safety checks</li>
        <li>All aspects of plumbing and heating</li>
        <li>Boiler breakdowns</li>
        <li>Flue sure reg number 804617</li>
      </ul>
      <div class="reg-badge" role="img" aria-label="Registration badge"></div>
    </div>
  </section>

</body>
</html>
```